Birchwell Commerce Business Card Design

Hello,

Attached you will find our logo. We are looking for a sharp business card design.

Other info to be included is:
Name: Marcus Doyle
Title: CEO
Office: (555) 014-2287
Cell: (555) 014-2287
E-mail address: marcus@birchwellcommerce.example
website: www.BirchwellCommerce.example

```html
<!DOCTYPE html>
<html lang="en">
<head>
<meta charset="utf-8">
<title>Birchwell Commerce — Business Card</title>
<link rel="stylesheet" href="https://fonts.googleapis.com/css2?family=Arimo:wght@400&family=Questrial&display=swap">
<style>
  :root {
    --accent-blue: #4a7ef0;
    --text-grey: #7b868c;
    --rule-grey: #a9b1b6;
    --bg-light: #f4f6fb;
    --bg-tint: #e4eaf4;
  }
  html, body {
    margin: 0;
    padding: 0;
    width: 1200px;
    height: 687px;
    overflow: hidden;
    background: #ffffff;
  }
  .card {
    position: relative;
    width: 1200px;
    height: 687px;
    overflow: hidden;
    font-family: "Arimo", Arial, sans-serif;
  }
  .card__backdrop {
    position: absolute;
    inset: 0;
    background: linear-gradient(125deg, var(--bg-tint) 0%, var(--bg-light) 45%, #fafbfd 100%);
  }
  .card__title {
    position: absolute;
    top: 38px;
    right: 75px;
    margin: 0;
    font-family: "Questrial", Arial, sans-serif;
    font-weight: 400;
    font-size: 108px;
    letter-spacing: 2px;
    line-height: 1;
    color: var(--accent-blue);
  }
  .card__name {
    position: absolute;
    left: 104px;
    top: 280px;
    margin: 0;
    font-weight: 400;
    font-size: 70px;
    line-height: 1;
    color: var(--text-grey);
    letter-spacing: -0.5px;
  }
  .card__name-last {
    color: var(--accent-blue);
  }
  .card__rule {
    position: absolute;
    left: 103px;
    top: 366px;
    width: 408px;
    height: 1px;
    background: var(--rule-grey);
  }
  .card__contacts {
    position: absolute;
    left: 107px;
    top: 432px;
    margin: 0;
    padding: 0;
    list-style: none;
    font-size: 43px;
    line-height: 56px;
    color: var(--text-grey);
  }
  .card__label {
    color: var(--accent-blue);
  }
</style>
</head>
<body>
  <div class="card">
    <div class="card__backdrop" role="img" aria-label="Soft pale blue geometric diamond pattern background"></div>

    <p class="card__title">CEO</p>

    <h1 class="card__name">Marcus <span class="card__name-last">Doyle</span></h1>
    <div class="card__rule"></div>

    <ul class="card__contacts">
      <li><span class="card__label">Tel:</span> (555) 014-2287</li>
      <li><span class="card__label">E-mail:</span> marcus@birchwellcommerce.example</li>
      <li><span class="card__label">Website:</span> www.birchwellcommerce.example</li>
    </ul>
  </div>
</body>
</html>
```